Tamsworth Counsel Cover 3 - Capital Allocation battlefield

Tamsworth Counsel is a business consulting firm. We will publish a series of four thought leadership pieces online and via PDF. The third of the series is attached to this project. We need an eye-catching cover page with a back page that keeps with our branding. The document attached is in the final draft, and the cover and pack pages are placeholders only. You can find more about our branding and style on our website www.tamsworthcounsel.com.au. The other three projects can be found here with a similar brief, and you are welcome to submit a design for all 4.

```html
<!DOCTYPE html>
<html lang="en">
<head>
<meta charset="utf-8">
<title>Tamsworth Counsel – The Capital Allocation Battlefield</title>
<link href="https://fonts.googleapis.com/css2?family=Poppins:wght@400;500;600;700;800&display=swap" rel="stylesheet">
<style>
  :root {
    --stage: #c0c0c0;
    --paper: #ffffff;
    --brand-blue: #00a6e8;
    --brand-orange: #f58a1f;
    --navy: #0c1650;
    --ink: #1e1e1e;
  }
  * { box-sizing: border-box; margin: 0; padding: 0; }
  html, body { width: 1200px; height: 1200px; overflow: hidden; }
  body { background: var(--stage); font-family: 'Poppins', sans-serif; position: relative; }

  .page { position: absolute; top: 220px; width: 538px; height: 763px; background: var(--paper); overflow: hidden; }
  .page--cover { left: 45px; }
  .page--back { left: 617px; }

  .brand { position: absolute; display: flex; align-items: center; gap: 10px; }
  .brand__dot { width: 30px; height: 30px; border-radius: 50%; background: var(--brand-orange); flex: none; }
  .brand__name { font-weight: 600; font-size: 25px; line-height: 1.05; color: var(--brand-blue); }

  /* cover */
  .cover-photo { position: absolute; left: 0; top: 28px; width: 538px; height: 650px;
    background: linear-gradient(115deg, #f7fafd 0%, #eaf2f9 30%, #b9d2e2 52%, #5f8a94 72%, #2f5560 100%); }
  .cover-photo::after { content: ""; position: absolute; left: 0; right: 0; bottom: 0; height: 70px;
    background: linear-gradient(180deg, rgba(255,255,255,0) 0%, #fff 100%); }
  .page--cover .brand { left: 42px; top: 58px; }
  .headline { position: absolute; left: 41px; top: 138px; font-weight: 800; font-size: 40px; line-height: 1.03; letter-spacing: -0.3px; }
  .headline span { display: block; }
  .headline__blue { color: var(--brand-blue); }
  .headline__dark { color: var(--ink); }
  .headline__orange { color: var(--brand-orange); font-size: 43px; }
  .subtitle { position: absolute; left: 41px; top: 274px; font-size: 15px; color: var(--ink); }
  .cover-url { position: absolute; left: 50px; top: 692px; font-size: 18px; letter-spacing: 2.4px; color: var(--ink); font-weight: 500; }
  .cover-url b, .back-url b { color: var(--brand-orange); font-weight: 600; }

  /* back */
  .back-photo { position: absolute; left: 0; top: 180px; width: 538px; height: 354px;
    background: linear-gradient(180deg, #ffffff 0%, #e4e6e8 30%, #aeb9c2 65%, #8193a2 100%); }
  .page--back .brand { left: 50%; transform: translateX(-50%); top: 62px; }
  .contact-title { position: absolute; top: 144px; width: 100%; text-align: center; font-weight: 700; font-size: 18px; color: var(--navy); }
  .contact-lead { position: absolute; top: 172px; width: 100%; text-align: center; font-size: 12.5px; line-height: 15px; color: var(--ink); }
  .contact-band { position: absolute; left: 0; top: 534px; width: 538px; height: 113px; background: var(--brand-blue); }
  .person { position: absolute; top: 22px; color: #fff; }
  .person--one { left: 38px; }
  .person--two { left: 285px; }
  .person__name { font-weight: 700; font-size: 13.5px; color: var(--navy); line-height: 15px; }
  .person__role { font-size: 11.5px; color: var(--navy); line-height: 14px; }
  .person__line { display: flex; align-items: center; gap: 6px; font-size: 12px; margin-top: 6px; }
  .person__line:first-of-type { margin-top: 9px; }
  .icon { width: 18px; height: 18px; flex: none; }
  .follow-band { position: absolute; left: 0; top: 647px; width: 538px; height: 116px; background: var(--navy); text-align: center; }
  .follow { margin-top: 14px; display: flex; justify-content: center; align-items: center; gap: 6px; }
  .follow__label { color: var(--brand-blue); font-weight: 500; font-size: 17px; }
  .follow__chip { width: 11px; height: 11px; background: var(--brand-orange); }
  .follow__handle { color: #fff; font-size: 11.5px; font-weight: 500; }
  .back-url { display: block; margin-top: 4px; color: #fff; font-size: 17px; letter-spacing: 2.4px; font-weight: 500; }
</style>
</head>
<body>

<section class="page page--cover">
  <div class="cover-photo" role="img" aria-label="Upward view of curved glass skyscrapers and green-clad residential towers against a pale sky"></div>
  <div class="brand"><span class="brand__dot"></span><span class="brand__name">Tamsworth<br>Counsel</span></div>
  <h1 class="headline">
    <span class="headline__blue">THE CAPITAL</span>
    <span class="headline__dark">ALLOCATION</span>
    <span class="headline__orange">BATTLEFIELD</span>
  </h1>
  <p class="subtitle">Deploying the War Chest</p>
  <p class="cover-url">www.<b>tamsworthcounsel</b>.com.au</p>
</section>

<section class="page page--back">
  <div class="back-photo" role="img" aria-label="Low-angle view of a modern glass office tower under a grey cloudy sky"></div>
  <div class="brand"><span class="brand__dot"></span><span class="brand__name">Tamsworth<br>Counsel</span></div>
  <h2 class="contact-title">CONTACT US</h2>
  <p class="contact-lead">To find out how Tamsworth Counsel can help<br>build your company into a market leader</p>

  <div class="contact-band">
    <div class="person person--one">
      <p class="person__name">EDWIN TAMSWORTH</p>
      <p class="person__role">Managing Director</p>
      <p class="person__line">
        <svg class="icon" viewBox="0 0 18 18"><circle cx="9" cy="9" r="9" fill="#f58a1f"/><path d="M6 4.8l1.6 1.9-.9 1.2c.6 1.3 1.5 2.2 2.8 2.8l1.2-.9 1.9 1.6-.9 1.5c-3.6-.3-6.3-3-6.6-6.6z" fill="#fff"/></svg>
        +61 400 555 018</p>
      <p class="person__line">
        <svg class="icon" viewBox="0 0 18 18"><circle cx="9" cy="9" r="9" fill="#f58a1f"/><rect x="4.5" y="6" width="9" height="6.2" rx="0.6" fill="#fff"/><path d="M4.8 6.3L9 9.4l4.2-3.1" stroke="#f58a1f" stroke-width="0.9" fill="none"/></svg>
        edwin@tamsworthcounsel.com.au</p>
    </div>
    <div class="person person--two">
      <p class="person__name">ROWAN TAMSWORTH</p>
      <p class="person__role">Managing Director</p>
      <p class="person__line">
        <svg class="icon" viewBox="0 0 18 18"><circle cx="9" cy="9" r="9" fill="#f58a1f"/><path d="M6 4.8l1.6 1.9-.9 1.2c.6 1.3 1.5 2.2 2.8 2.8l1.2-.9 1.9 1.6-.9 1.5c-3.6-.3-6.3-3-6.6-6.6z" fill="#fff"/></svg>
        +61 400 555 027</p>
      <p class="person__line">
        <svg class="icon" viewBox="0 0 18 18"><circle cx="9" cy="9" r="9" fill="#f58a1f"/><rect x="4.5" y="6" width="9" height="6.2" rx="0.6" fill="#fff"/><path d="M4.8 6.3L9 9.4l4.2-3.1" stroke="#f58a1f" stroke-width="0.9" fill="none"/></svg>
        rowan@tamsworthcounsel.com.au</p>
    </div>
  </div>

  <div class="follow-band">
    <div class="follow">
      <span class="follow__label">Follow us</span>
      <span class="follow__chip"></span><span class="follow__chip"></span>
      <span class="follow__handle">@edwin-tamsworth</span>
    </div>
    <span class="back-url">www.<b>tamsworthcounsel</b>.com.au</span>
  </div>
</section>

</body>
</html>
```